Funny Real Estate Marketing Banner Ad

I'm a Real Estate agent in Vancouver, BC. I've provided 3 photos, two recent (one in colour and one in black & white) and one from 1990. I'd like an ad with a catchy tagline, e.g. (Keeping it "real" estate since the 90's), integrating one recent and one past photo. The ad should be funny but professional. It will need to be in a few different formats (320 x250, 320 x 50, 1200 x 628 & 728 x 90). It might be preferable to use the existing black and white photo, given that they look more similar.
Updates

Target Market(s)

Home Buyers and Sellers

Industry/Entity Type

Real Estate Agent

Requirements
Must have
• Would like it to match my current website colours - www.agentmorvyn.net.
• Catchy Tagline.
• My Name, phone # and web address.

```html
<!DOCTYPE html>
<html lang="en">
<head>
<meta charset="utf-8">
<title>Morvyn Ashdale – Banner Set</title>
<link rel="stylesheet" href="https://fonts.googleapis.com/css2?family=Roboto+Condensed:wght@700&family=Arimo:wght@400;700&family=Cinzel:wght@400&display=swap">
<style>
:root{
  --page:#e4e6ea;
  --blue:#1a63d0;
  --blue-deep:#0a3690;
  --blue-bright:#3a9cf5;
  --ring:#0d47b8;
  --gold:#f6c400;
  --gold-edge:#c99400;
  --phone:#d3201d;
  --white:#ffffff;
  --ribbon:#d8221c;
  --wall:#f2f1ee;
  --wall-shade:#d9d6d1;
  --wood:#a8733f;
  --floor:#7d7c7a;
  --figure:#3c3c3c;
  --photo-a:#f0eeea;
  --photo-b:#c5bdb2;
  --photo-c:#5e4c3b;
}
*{box-sizing:border-box;margin:0;padding:0}
html,body{width:1200px;height:1200px;overflow:hidden}
body{background:var(--page);position:relative;font-family:"Arimo",Arial,sans-serif}

.banner{position:absolute;overflow:hidden;color:var(--white);
  background:radial-gradient(ellipse at 30% 75%,var(--blue-bright) 0%,var(--blue) 45%,var(--blue-deep) 100%);
  box-shadow:0 18px 22px -14px rgba(0,0,0,.45)}
.banner--medium{left:172px;top:24px;width:443px;height:370px}
.banner--mobile{left:688px;top:322px;width:468px;height:72px}
.banner--leader{left:172px;top:454px;width:866px;height:108px}
.banner--social{left:164px;top:628px;width:882px;height:460px}

.url{position:absolute;font-size:13px;color:var(--white)}
.photo{position:absolute;background:linear-gradient(180deg,var(--wall) 0%,var(--wall-shade) 55%,var(--photo-c) 100%)}
.portrait{position:absolute;border-radius:50%;border:9px solid var(--ring);overflow:hidden;
  background:
    radial-gradient(ellipse 30% 45% at 62% 78%,var(--figure) 0%,rgba(60,60,60,.85) 55%,rgba(60,60,60,0) 100%),
    linear-gradient(90deg,rgba(168,115,63,0) 55%,rgba(168,115,63,.75) 78%,rgba(120,80,45,.85) 100%),
    linear-gradient(180deg,var(--wall) 0%,var(--wall) 40%,var(--wall-shade) 62%,var(--floor) 100%)}
.headline{position:absolute;font-family:"Roboto Condensed","Arial Narrow",sans-serif;font-weight:700;
  line-height:1.1;text-align:center;white-space:nowrap;text-shadow:0 2px 3px rgba(0,0,0,.35)}
.since{position:absolute;font-family:"Arimo",Arial,sans-serif;text-align:center;white-space:nowrap}
.phone{position:absolute;display:flex;align-items:center;justify-content:center;
  background:linear-gradient(var(--gold),#eeb000);border:2px solid var(--gold-edge);
  border-radius:10px;color:var(--phone);font-weight:700;box-shadow:0 3px 5px rgba(0,0,0,.35)}
.name{position:absolute;font-family:"Cinzel",Georgia,serif;color:var(--white);
  text-shadow:0 1px 3px rgba(0,0,0,.7);white-space:nowrap}

.listing{position:absolute;background:var(--white);overflow:hidden}
.listing .photo{left:6px;right:6px;top:22%;bottom:18%}
.listing .tag{position:absolute;left:-16px;top:6px;width:60px;height:12px;background:var(--ribbon);
  transform:rotate(-45deg);font-size:6px;font-weight:700;text-align:center;line-height:12px}

.strip{position:absolute;left:0;right:0;background:var(--blue-deep)}
.caption{position:absolute;left:0;width:1200px;top:1128px;text-align:center;
  font-family:"Roboto Condensed","Arial Narrow",sans-serif;font-weight:700;font-size:40px;
  color:var(--white);text-shadow:0 0 3px #333,0 2px 4px rgba(0,0,0,.6)}
</style>
</head>
<body>

<!-- 320 x 250 -->
<section class="banner banner--medium">
  <div class="strip" style="top:0;height:52px"></div>
  <span class="url" style="left:10px;top:8px">www.agentmorvyn.net</span>
  <div class="listing" style="left:0;top:54px;width:105px;height:102px"><div class="photo" role="img" aria-label="Sold listing: bedroom interior"></div><span class="tag">SOLD</span></div>
  <div class="listing" style="left:108px;top:54px;width:80px;height:102px"><div class="photo" role="img" aria-label="Sold listing: living room interior"></div><span class="tag">SOLD</span></div>
  <div class="portrait" role="img" aria-label="Black and white portrait of the agent in a modern apartment" style="left:202px;top:-60px;width:440px;height:440px"></div>
  <div class="headline" style="left:0;width:200px;top:182px;font-size:30px">Keeping it<br>"real" estate</div>
  <div class="since" style="left:0;width:200px;top:260px;font-size:20px">since the 90's</div>
  <div class="phone" style="left:26px;top:306px;width:154px;height:44px;font-size:16px">(604) 555-0148</div>
  <span class="name" style="right:10px;bottom:24px;font-size:21px">Morvyn Ashdale</span>
</section>

<!-- 320 x 50 -->
<section class="banner banner--mobile">
  <div class="portrait" role="img" aria-label="Black and white portrait of the agent" style="left:272px;top:-80px;width:260px;height:230px;border-width:5px"></div>
  <div class="headline" style="left:14px;top:5px;font-size:21px;text-align:left">Keeping it "real" estate</div>
  <div class="phone" style="left:12px;top:34px;width:98px;height:28px;font-size:11px;border-radius:7px">(604) 555-0148</div>
  <div class="since" style="left:140px;top:30px;width:110px;font-size:14px">since the 90's</div>
  <span class="url" style="left:128px;top:53px;font-size:10px;font-weight:700">www.agentmorvyn.net</span>
  <span class="name" style="right:8px;bottom:4px;font-size:17px">Morvyn Ashdale</span>
</section>

<!-- 728 x 90 -->
<section class="banner banner--leader">
  <span class="url" style="left:14px;top:8px">www.agentmorvyn.net</span>
  <div class="phone" style="left:24px;top:42px;width:126px;height:38px;font-size:13px">(604) 555-0148</div>
  <div class="listing" style="left:182px;top:0;width:110px;height:108px;border-left:4px solid var(--blue-deep)"><div class="photo" role="img" aria-label="Sold listing: bedroom interior"></div><span class="tag">SOLD</span></div>
  <div class="portrait" role="img" aria-label="Black and white portrait of the agent in a modern apartment" style="left:508px;top:-190px;width:520px;height:460px"></div>
  <div class="headline" style="left:298px;width:200px;top:10px;font-size:26px">Keeping it<br>"real" estate</div>
  <div class="since" style="left:298px;width:200px;top:74px;font-size:16px">since the 90's</div>
  <span class="name" style="right:18px;bottom:8px;font-size:23px">Morvyn Ashdale</span>
</section>

<!-- 1200 x 628 -->
<section class="banner banner--social">
  <div class="strip" style="top:0;height:70px;background:linear-gradient(var(--blue),var(--blue-deep))"></div>
  <div class="strip" style="top:70px;height:170px;background:var(--blue-deep);border-top:3px solid var(--blue-bright);border-bottom:3px solid var(--blue-bright)"></div>
  <span class="url" style="left:28px;top:18px;font-size:15px">www.agentmorvyn.net</span>
  <div class="listing" style="left:12px;top:84px;width:136px;height:140px"><div class="photo" role="img" aria-label="Sold listing: bedroom interior"></div><span class="tag">SOLD</span></div>
  <div class="listing" style="left:153px;top:84px;width:145px;height:140px"><div class="photo" role="img" aria-label="Sold listing: open living room"></div><span class="tag">SOLD</span></div>
  <div class="listing" style="left:303px;top:84px;width:143px;height:140px"><div class="photo" role="img" aria-label="Sold listing: high-rise tower"></div><span class="tag">SOLD</span></div>
  <div class="listing" style="left:451px;top:84px;width:143px;height:140px"><div class="photo" role="img" aria-label="Sold listing: townhouse exterior"></div><span class="tag">SOLD</span></div>
  <div class="portrait" role="img" aria-label="Black and white portrait of the agent in a modern apartment" style="left:520px;top:-50px;width:600px;height:600px;border-width:14px"></div>
  <div class="headline" style="left:30px;top:280px;font-size:42px;text-align:left">Keeping it "real" estate</div>
  <div class="since" style="left:276px;top:338px;font-size:25px;text-align:left">since the 90's</div>
  <div class="phone" style="left:46px;top:380px;width:216px;height:64px;font-size:22px;border-radius:12px">(604) 555-0148</div>
  <span class="name" style="right:14px;bottom:42px;font-size:30px">Morvyn Ashdale</span>
</section>

<div class="caption">320 x250, 320 x 50, 1200 x 628, 728 x 90</div>

</body>
</html>
```